Memento Mori Calendar

I’m looking for a graphic designer to create a Memento Mori–style life calendar that captures the essence of OLVENTRA — minimal, timeless, and deeply philosophical.

The design should be black and white only, with a refined, clean aesthetic and a sense of stillness and precision.
It should feel modern yet eternal, reflecting the themes of time, mortality, and presence.

Deliverables (Print-Ready Files):

24 x 30 in

24 x 32 in

24 x 36 in

A1 (594 x 841 mm)

All formats should be high-resolution and ready for professional printing (300 DPI, CMYK).

Design Requirements:

The calendar layout should follow the Memento Mori life calendar concept (weeks of life represented as small squares or circles).

The overall tone: minimal, meditative, monochrome.

Include the brand name: OLVENTRA (in an elegant, understated placement).

Add the following quote at the bottom or in a subtle position:

“Life can only be understood backwards; but it must be lived forwards.”
— Henrik Vastmoe

Target Market(s)

The OLVENTRA audience consists of urban, creative individuals aged 25 to 45, belonging to a middle to upper-middle income class. They lead conscious, quietly ambitious lives, seeking balance between inner depth and modern design. Their values center on awareness, presence, authenticity, and emotional depth, reflected in their preference for a monochrome, minimal, and timeless aesthetic. They tend to be introverted, reflective, and spiritually curious, drawn to brands that embody meaning and restraint rather than excess. Their cultural and stylistic affinities include Pyrel, Tulve, Ni Ostra, The Quiet Bench Guild, Durvanne, and Ombrix — labels that share OLVENTRAs devotion to simplicity, substance, and subtle ritual.

Font styles to use
Serif
Sans Serif

Colors

Designer to choose only greyscale colors for use in the design.

Requirements
Must have
• The calendar layout should follow the Memento Mori life calendar concept (weeks of life represented as small squares or circles). The overall tone: minimal, meditative, monochrome. Include the brand name: qrnvalto (in an elegant, understated placement). Add the following quote at the bottom or in a subtle position: “Life can only be understood backwards; but it must be lived forwards.” — Henrik Vastmoe

```html
<!DOCTYPE html>
<html lang="en">
<head>
<meta charset="utf-8">
<title>QRNVALTO · Memento Mori Life Calendar</title>
<link rel="stylesheet" href="https://fonts.googleapis.com/css2?family=Cinzel:wght@600&family=Crimson+Pro:ital,wght@1,400;1,700&family=Inter:wght@500;700;800&family=Syncopate:wght@700&display=swap">
<style>
  :root {
    --ink: #111111;
    --frame-outer: #333333;
    --frame-inner: #7a7a7a;
    --banner: #777777;
    --rule: #7a7a7a;
    --paper: #ffffff;
  }
  html, body {
    margin: 0;
    padding: 0;
    width: 907px;
    height: 1200px;
    overflow: hidden;
    background: var(--paper);
  }
  .poster { display: block; width: 907px; height: 1200px; }
  .frame-outer { fill: none; stroke: var(--frame-outer); stroke-width: 3.5; }
  .frame-inner { fill: none; stroke: var(--frame-inner); stroke-width: 2; }
  .brand-band { fill: var(--banner); }
  .brand-name { font-family: "Syncopate", "Arial Black", sans-serif; font-weight: 700; fill: var(--paper); font-size: 29px; }
  .week-rule { stroke: var(--ink); stroke-width: 3; }
  .week-label { font-family: "Inter", Arial, sans-serif; font-weight: 800; font-size: 15px; fill: var(--ink); }
  .years-label { font-family: "Inter", Arial, sans-serif; font-weight: 800; font-size: 11.5px; fill: var(--ink); }
  .spine-rule { stroke: var(--rule); stroke-width: 2; }
  .title { font-family: "Cinzel", "Times New Roman", serif; font-weight: 600; font-size: 78px; fill: var(--ink); }
  .week-box { fill: none; stroke: #222222; stroke-width: 0.75; }
  .col-num { font-family: "Inter", Arial, sans-serif; font-weight: 500; font-size: 4.6px; fill: var(--ink); text-anchor: middle; }
  .col-num.major { font-size: 8.5px; font-weight: 700; }
  .row-num { font-family: "Inter", Arial, sans-serif; font-weight: 500; font-size: 4.6px; fill: var(--ink); text-anchor: end; }
  .row-num.decade { font-size: 9px; font-weight: 700; }
  .quote { font-family: "Crimson Pro", Georgia, serif; font-style: italic; font-weight: 400; font-size: 16px; fill: var(--ink); text-anchor: end; }
  .quote-author { font-family: "Crimson Pro", Georgia, serif; font-style: italic; font-weight: 700; font-size: 15px; fill: var(--ink); text-anchor: end; }
</style>
</head>
<body>
<svg class="poster" viewBox="0 0 907 1200" xmlns="http://www.w3.org/2000/svg">
  <defs>
    <pattern id="week-cell-left" patternUnits="userSpaceOnUse" x="216" y="0" width="10.62" height="10.64">
      <rect class="week-box" x="0.5" y="0.5" width="7" height="7" rx="1.6"/>
    </pattern>
    <pattern id="week-cell-right" patternUnits="userSpaceOnUse" x="505.4" y="0" width="10.62" height="10.64">
      <rect class="week-box" x="0.5" y="0.5" width="7" height="7" rx="1.6"/>
    </pattern>
    <g id="decade-grid">
      <rect x="216" y="0" width="276.2" height="106.4" fill="url(#week-cell-left)"/>
      <rect x="505.4" y="0" width="276.2" height="106.4" fill="url(#week-cell-right)"/>
    </g>
  </defs>

  <!-- frames -->
  <rect class="frame-outer" x="78" y="69" width="754" height="1055" rx="16"/>
  <rect class="frame-inner" x="94" y="83" width="722" height="1027" rx="6"/>

  <!-- brand band -->
  <polygon class="brand-band" points="96,98 461,98 473,144 96,144"/>
  <text class="brand-name" x="134" y="134" textLength="298" lengthAdjust="spacingAndGlyphs">QRNVALTO</text>

  <!-- week name line -->
  <line class="week-rule" x1="480" y1="142" x2="719" y2="142"/>
  <text class="week-label" x="725" y="145">WEEK</text>

  <!-- spine -->
  <text class="years-label" transform="translate(187,163) rotate(90)">YEARS</text>
  <line class="spine-rule" x1="191.5" y1="235" x2="191.5" y2="1104"/>
  <text class="title" transform="translate(177,979) rotate(-90)" textLength="712" lengthAdjust="spacingAndGlyphs">MOMENTO MORI</text>

  <!-- week numbers -->
  <g class="week-numbers">
    <text class="col-num" x="219.9" y="165">1</text><text class="col-num" x="230.5" y="165">2</text><text class="col-num" x="241.1" y="165">3</text><text class="col-num" x="251.8" y="165">4</text><text class="col-num major" x="262.4" y="166">5</text><text class="col-num" x="273" y="165">6</text><text class="col-num" x="283.6" y="165">7</text><text class="col-num" x="294.2" y="165">8</text><text class="col-num" x="304.9" y="165">9</text><text class="col-num major" x="315.5" y="166">10</text><text class="col-num" x="326.1" y="165">11</text><text class="col-num" x="336.7" y="165">12</text><text class="col-num" x="347.3" y="165">13</text><text class="col-num" x="358" y="165">14</text><text class="col-num major" x="368.6" y="166">15</text><text class="col-num" x="379.2" y="165">16</text><text class="col-num" x="389.8" y="165">17</text><text class="col-num" x="400.4" y="165">18</text><text class="col-num" x="411.1" y="165">19</text><text class="col-num major" x="421.7" y="166">20</text><text class="col-num" x="432.3" y="165">21</text><text class="col-num" x="442.9" y="165">22</text><text class="col-num" x="453.5" y="165">23</text><text class="col-num" x="464.2" y="165">24</text><text class="col-num major" x="474.8" y="166">25</text><text class="col-num" x="485.4" y="165">26</text>
    <text class="col-num" x="509.3" y="165">27</text><text class="col-num" x="519.9" y="165">28</text><text class="col-num" x="530.5" y="165">29</text><text class="col-num major" x="541.2" y="166">30</text><text class="col-num" x="551.8" y="165">31</text><text class="col-num" x="562.4" y="165">32</text><text class="col-num" x="573" y="165">33</text><text class="col-num" x="583.6" y="165">34</text><text class="col-num major" x="594.3" y="166">35</text><text class="col-num" x="604.9" y="165">36</text><text class="col-num" x="615.5" y="165">37</text><text class="col-num" x="626.1" y="165">38</text><text class="col-num" x="636.7" y="165">39</text><text class="col-num major" x="647.4" y="166">40</text><text class="col-num" x="658" y="165">41</text><text class="col-num" x="668.6" y="165">42</text><text class="col-num" x="679.2" y="165">43</text><text class="col-num" x="689.8" y="165">44</text><text class="col-num major" x="700.5" y="166">45</text><text class="col-num" x="711.1" y="165">46</text><text class="col-num" x="721.7" y="165">47</text><text class="col-num" x="732.3" y="165">48</text><text class="col-num" x="742.9" y="165">49</text><text class="col-num major" x="753.6" y="166">50</text><text class="col-num" x="764.2" y="165">51</text><text class="col-num" x="774.8" y="165">52</text>
  </g>

  <!-- decades of weeks -->
  <g class="decade" transform="translate(0,169.7)">
    <use href="#decade-grid"/>
    <text class="row-num" x="209" y="5.6">1</text><text class="row-num" x="209" y="16.2">2</text><text class="row-num" x="209" y="26.9">3</text><text class="row-num" x="209" y="37.5">4</text><text class="row-num" x="209" y="48.2">5</text><text class="row-num" x="209" y="58.8">6</text><text class="row-num" x="209" y="69.4">7</text><text class="row-num" x="209" y="80.1">8</text><text class="row-num" x="209" y="90.7">9</text><text class="row-num decade" x="210" y="104">10</text>
  </g>
  <g class="decade" transform="translate(0,283.4)">
    <use href="#decade-grid"/>
    <text class="row-num" x="209" y="5.6">11</text><text class="row-num" x="209" y="16.2">12</text><text class="row-num" x="209" y="26.9">13</text><text class="row-num" x="209" y="37.5">14</text><text class="row-num" x="209" y="48.2">15</text><text class="row-num" x="209" y="58.8">16</text><text class="row-num" x="209" y="69.4">17</text><text class="row-num" x="209" y="80.1">18</text><text class="row-num" x="209" y="90.7">19</text><text class="row-num decade" x="210" y="104">20</text>
  </g>
  <g class="decade" transform="translate(0,397.1)">
    <use href="#decade-grid"/>
    <text class="row-num" x="209" y="5.6">21</text><text class="row-num" x="209" y="16.2">22</text><text class="row-num" x="209" y="26.9">23</text><text class="row-num" x="209" y="37.5">24</text><text class="row-num" x="209" y="48.2">25</text><text class="row-num" x="209" y="58.8">26</text><text class="row-num" x="209" y="69.4">27</text><text class="row-num" x="209" y="80.1">28</text><text class="row-num" x="209" y="90.7">29</text><text class="row-num decade" x="210" y="104">30</text>
  </g>
  <g class="decade" transform="translate(0,510.8)">
    <use href="#decade-grid"/>
    <text class="row-num" x="209" y="5.6">31</text><text class="row-num" x="209" y="16.2">32</text><text class="row-num" x="209" y="26.9">33</text><text class="row-num" x="209" y="37.5">34</text><text class="row-num" x="209" y="48.2">35</text><text class="row-num" x="209" y="58.8">36</text><text class="row-num" x="209" y="69.4">37</text><text class="row-num" x="209" y="80.1">38</text><text class="row-num" x="209" y="90.7">39</text><text class="row-num decade" x="210" y="104">40</text>
  </g>
  <g class="decade" transform="translate(0,624.5)">
    <use href="#decade-grid"/>
    <text class="row-num" x="209" y="5.6">41</text><text class="row-num" x="209" y="16.2">42</text><text class="row-num" x="209" y="26.9">43</text><text class="row-num" x="209" y="37.5">44</text><text class="row-num" x="209" y="48.2">45</text><text class="row-num" x="209" y="58.8">46</text><text class="row-num" x="209" y="69.4">47</text><text class="row-num" x="209" y="80.1">48</text><text class="row-num" x="209" y="90.7">49</text><text class="row-num decade" x="210" y="104">50</text>
  </g>
  <g class="decade" transform="translate(0,738.2)">
    <use href="#decade-grid"/>
    <text class="row-num" x="209" y="5.6">51</text><text class="row-num" x="209" y="16.2">52</text><text class="row-num" x="209" y="26.9">53</text><text class="row-num" x="209" y="37.5">54</text><text class="row-num" x="209" y="48.2">55</text><text class="row-num" x="209" y="58.8">56</text><text class="row-num" x="209" y="69.4">57</text><text class="row-num" x="209" y="80.1">58</text><text class="row-num" x="209" y="90.7">59</text><text class="row-num decade" x="210" y="104">60</text>
  </g>
  <g class="decade" transform="translate(0,851.9)">
    <use href="#decade-grid"/>
    <text class="row-num" x="209" y="5.6">61</text><text class="row-num" x="209" y="16.2">62</text><text class="row-num" x="209" y="26.9">63</text><text class="row-num" x="209" y="37.5">64</text><text class="row-num" x="209" y="48.2">65</text><text class="row-num" x="209" y="58.8">66</text><text class="row-num" x="209" y="69.4">67</text><text class="row-num" x="209" y="80.1">68</text><text class="row-num" x="209" y="90.7">69</text><text class="row-num decade" x="210" y="104">70</text>
  </g>
  <g class="decade" transform="translate(0,965.6)">
    <use href="#decade-grid"/>
    <text class="row-num" x="209" y="5.6">71</text><text class="row-num" x="209" y="16.2">72</text><text class="row-num" x="209" y="26.9">73</text><text class="row-num" x="209" y="37.5">74</text><text class="row-num" x="209" y="48.2">75</text><text class="row-num" x="209" y="58.8">76</text><text class="row-num" x="209" y="69.4">77</text><text class="row-num" x="209" y="80.1">78</text><text class="row-num" x="209" y="90.7">79</text><text class="row-num decade" x="210" y="104">80</text>
  </g>

  <!-- quote -->
  <text class="quote" x="778" y="1090">“Life can only be understood backwards; but it must be lived forwards.”</text>
  <rect x="638" y="1100" width="144" height="16" fill="var(--paper)"/>
  <text class="quote-author" x="778" y="1110">Henrik Vastmoe</text>
</svg>
</body>
</html>
```